Professional BIO Template with photo and logo

Hello,
I need a professional Bio template developed via Microsoft WORD ASAP!!!!! I would like to just be able to add the text I need to add. So resize-able text boxes. Potentially able to adjust the font. These are the things I need added it to include.
Head shot (attached)
Text Box for Name
Text Box for phone number
Text box for email
KTW Logo (attached)
Maybe a blue banner at the top or some background boxes that are blue or grey. Here are the pantone colors that our company uses.

CORE COLOR
100c 91m 17y 6k 38r 58g 128b Hex #263A80 Pantone 7687 C

CORE CONTRAST COLOR
36c 29m 28y 0k 168r 168g 170b Hex #669999 Pantone Cool Gray 6C

I also attached some examples of what we have been looking at. Instead of green add the blue...instead of black maybe just be white.

Thank you

```html
<!DOCTYPE html>
<html lang="en">
<head>
<meta charset="utf-8">
<title>Evan Marlow – Bio</title>
<link rel="stylesheet" href="https://fonts.googleapis.com/css2?family=EB+Garamond:wght@600&family=Tinos:wght@400;700&display=swap">
<style>
  :root {
    --core-blue: #263A80;
    --backdrop: #5f5f5f;
    --paper: #ffffff;
    --rule-grey: #a8a8aa;
    --teal: #669999;
    --ink: #1c1c1c;
    --white: #ffffff;
    --watermark: #eef0f5;
  }
  * { margin: 0; padding: 0; box-sizing: border-box; }
  html, body {
    width: 1095px; height: 1200px; overflow: hidden;
    background: var(--backdrop);
  }
  .bio-page {
    position: absolute; left: 202px; top: 85px;
    width: 735px; height: 1039px;
    background: var(--paper);
    overflow: hidden;
    font-family: "Tinos", "Times New Roman", serif;
  }
  .header-band {
    position: absolute; left: 0; top: 0; width: 100%; height: 266px;
    background: var(--core-blue);
    border-bottom: 3px solid var(--rule-grey);
  }
  .company-name {
    position: absolute; left: 405px; top: 16px; width: 150px; height: 119px;
    display: flex; align-items: center; justify-content: center;
    font-family: "Tinos", "Times New Roman", serif;
    font-weight: 700; font-size: 46px; letter-spacing: 3px;
    color: var(--white);
  }
  .header-divider {
    position: absolute; left: 566px; top: 13px; width: 2px; height: 126px;
    background: var(--white);
  }
  .contact-list {
    position: absolute; left: 575px; top: 24px;
    color: var(--white); font-size: 10.8px; line-height: 13px;
    list-style: none;
  }
  .contact-item { position: relative; padding-left: 17px; margin-bottom: 9.6px; }
  .contact-item svg { position: absolute; left: 0; top: 1px; }
  .contact-item strong { font-weight: 700; }
  .person-name {
    position: absolute; left: 247px; top: 178px;
    font-family: "EB Garamond", "Times New Roman", serif;
    font-weight: 600; font-size: 66px; line-height: 1;
    color: var(--white);
  }
  .headshot {
    position: absolute; left: 37px; top: 67px; width: 193px; height: 325px;
    border-radius: 97px;
    border: 6px solid var(--core-blue);
    background: linear-gradient(180deg, #3c3c3e 0%, #5a4a42 30%, #c98f72 45%, #2c2f3a 70%, #1b1e28 100%);
  }
  .watermark {
    position: absolute; left: 0; top: 520px; width: 100%;
    text-align: center;
    font-family: "Tinos", "Times New Roman", serif;
    font-weight: 700; font-size: 170px; letter-spacing: 24px;
    color: var(--watermark);
  }
  .bio-text {
    position: absolute; left: 38px; top: 415px; width: 671px;
    font-size: 15.4px; line-height: 17.76px; color: var(--ink);
    text-align: justify; hyphens: auto;
  }
  .bio-text p { margin-bottom: 17.76px; }
  .footer-band {
    position: absolute; left: 0; bottom: 0; width: 100%; height: 30px;
    background: var(--teal);
    border-top: 3px solid var(--rule-grey);
    display: flex; align-items: center; justify-content: center;
    font-size: 9px; font-weight: 700; letter-spacing: 5px;
    color: var(--ink);
  }
</style>
</head>
<body>
<main class="bio-page">
  <header class="header-band">
    <div class="company-name">KTW</div>
    <div class="header-divider"></div>
    <ul class="contact-list">
      <li class="contact-item">
        <svg width="9" height="12" viewBox="0 0 10 13"><path d="M5 0a5 5 0 0 0-5 5c0 3.5 5 8 5 8s5-4.5 5-8a5 5 0 0 0-5-5zm0 7a2 2 0 1 1 0-4 2 2 0 0 1 0 4z" fill="#fff"/></svg>
        218 Ridgeview Avenue<br>Suite 300<br><strong>Lakewood, CO 80226</strong>
      </li>
      <li class="contact-item">
        <svg width="11" height="11" viewBox="0 0 12 12"><path d="M2.5 1l2 2.5-1.2 1.2a7 7 0 0 0 3.9 3.9L8.4 7.4 11 9.5 9.8 11C5 11 1 7 1 2.2z" fill="#fff"/></svg>
        <strong>Phone</strong>: 303-555-0147<br><strong>Fax</strong>: 303-555-0162
      </li>
      <li class="contact-item">
        <svg width="10" height="8" viewBox="0 0 11 9" style="top:3px"><rect width="11" height="9" rx="1" fill="#fff"/><path d="M0.5 1l5 4 5-4" stroke="#263A80" fill="none" stroke-width="1"/></svg>
        evanmarlow@mail.com
      </li>
    </ul>
    <h1 class="person-name">Evan Marlow</h1>
  </header>

  <div class="headshot" role="img" aria-label="Head shot of Evan Marlow"></div>

  <div class="watermark" aria-hidden="true">KTW</div>

  <section class="bio-text">
    <p>Lorem Ipsum is simply dummy text of the printing and typesetting industry. Lorem Ipsum has been the industry's standard dummy text ever since the 1500s, when an unknown printer took a galley of type and scrambled it to make a type specimen book. It has survived not only five centuries, but also the leap into electronic typesetting, remaining essentially unchanged. It was popularised in the 1960s with the release of Typeline sheets containing Lorem Ipsum passages, and more recently with desktop publishing software like Norvo Pagesetter including versions of Lorem Ipsum.</p>
    <p>Lorem Ipsum is simply dummy text of the printing and typesetting industry. Lorem Ipsum has been the industry's standard dummy text ever since the 1500s, when an unknown printer took a galley of type and scrambled it to make a type specimen book. It has survived not only five centuries, but also the leap into electronic typesetting, remaining essentially unchanged. It was popularised in the 1960s with the release of Typeline sheets containing Lorem Ipsum passages, and more recently with desktop publishing software like Norvo Pagesetter including versions of Lorem Ipsum.</p>
    <p>Lorem Ipsum is simply dummy text of the printing and typesetting industry. Lorem Ipsum has been the industry's standard dummy text ever since the 1500s, when an unknown printer took a galley of type and scrambled it to make a type specimen book. It has survived not only five centuries, but also the leap into electronic typesetting, remaining essentially unchanged. It was popularised in the 1960s with the release of Typeline sheets containing Lorem Ipsum passages, and more recently with desktop publishing software like Norvo Pagesetter including versions of Lorem Ipsum.</p>
    <p>Lorem Ipsum is simply dummy text of the printing and typesetting industry. Lorem Ipsum has been the industry's standard dummy text ever since the 1500s, when an unknown printer took a galley of type and scrambled it to make a type specimen book. It has survived not only five centuries, but also the leap into electronic typesetting, remaining essentially unchanged. It was popularised in the 1960s with the release of Typeline sheets containing Lorem Ipsum passages, and more recently with desktop publishing software like Norvo Pagesetter including versions of Lorem Ipsum.</p>
    <p>Lorem Ipsum is simply dummy text of the printing and typesetting industry. Lorem Ipsum has been the industry's standard dummy text ever since the containing Lorem Ipsum passages, and more recently with desktop publishing software like Norvo Pagesetter including versions of Lorem Ipsum.</p>
  </section>

  <footer class="footer-band">WWW.KTWINC.COM</footer>
</main>
</body>
</html>
```